Design an App Mockup for a Gym

Hi, I just need the design of the app, I need the files in Illustrator (.ai ) or Photoshop. So I can modify things later.

design 1- Home (Welcome/log in/sign up)
2- Register your name, age, weight,height,id number, gender
3-confirmation window and message to check email to verify your account
4-Your profile and 3 options to choose if you want to loose weight, fit, build muscle.
5- Calendar with different routines everyday
6-View your progress of the week

you can add more windows if you want , create new things. The design should be attractive, modern, and cool. The target market is students.

I will attach a very basic sketch

I will choose the winner of the contest tonight, I need it before 4am (-6)

```html
<!DOCTYPE html>
<html lang="es">
<head>
<meta charset="utf-8">
<title>Nova Gym – Bienvenido</title>
<link rel="stylesheet" href="https://fonts.googleapis.com/css2?family=Titillium+Web:wght@400;600&display=swap">
<style>
  :root {
    --page-bg: #efefef;
    --screen-edge: #0f4a2c;
    --screen-mid: #3f8f6e;
    --screen-glow: #86dcd6;
    --screen-blue: #6fb6e0;
    --panel-fill: rgba(255, 255, 255, 0.22);
    --title-fill: rgba(255, 255, 255, 0.18);
    --text-light: #ffffff;
    --figure-male: #8c3fcc;
    --figure-male-glow: rgba(190, 110, 255, 0.75);
    --figure-female: #d4167f;
    --tick-fill: #16b8c8;
    --button-top: #232c5a;
    --button-bottom: #55678f;
  }
  * { box-sizing: border-box; margin: 0; padding: 0; }
  html, body {
    width: 1200px;
    height: 1200px;
    overflow: hidden;
    background: var(--page-bg);
    font-family: "Titillium Web", Arial, sans-serif;
  }
  .app-screen {
    position: absolute;
    left: 280px;
    top: 33px;
    width: 640px;
    height: 1133px;
    overflow: hidden;
    background:
      radial-gradient(ellipse 55% 45% at 50% 52%, var(--screen-glow) 0%, rgba(134,220,214,0) 100%),
      radial-gradient(ellipse 40% 30% at 60% 75%, var(--screen-blue) 0%, rgba(111,182,224,0) 100%),
      radial-gradient(ellipse 80% 70% at 50% 50%, var(--screen-mid) 0%, var(--screen-edge) 100%);
  }
  .welcome-panel {
    position: absolute;
    left: 23px;
    top: 82px;
    width: 595px;
    height: 960px;
    background: var(--panel-fill);
    border-radius: 6px;
    color: var(--text-light);
  }
  .brand-title {
    position: absolute;
    left: 95px;
    top: 83px;
    width: 405px;
    height: 95px;
    background: var(--title-fill);
    font-size: 78px;
    font-weight: 400;
    line-height: 95px;
    text-align: center;
    letter-spacing: 1px;
    white-space: nowrap;
  }
  .greeting {
    position: absolute;
    left: 0;
    top: 218px;
    width: 100%;
    text-align: center;
    font-size: 45px;
    line-height: 60px;
    font-weight: 400;
  }
  .gender-option {
    position: absolute;
    top: 326px;
    border-radius: 40px 40px 10px 10px;
  }
  .gender-option.male {
    left: 143px;
    width: 82px;
    height: 256px;
    background: var(--figure-male);
    box-shadow: 0 0 22px 6px var(--figure-male-glow);
  }
  .gender-option.female {
    left: 380px;
    width: 98px;
    height: 261px;
    background: var(--figure-female);
  }
  .selected-tick {
    position: absolute;
    left: 181px;
    top: 509px;
    width: 49px;
    height: 49px;
  }
  .intro-copy {
    position: absolute;
    left: 0;
    top: 614px;
    width: 100%;
    font-size: 15px;
    line-height: 19.6px;
    text-align: center;
    white-space: nowrap;
  }
  .sign-on-button {
    position: absolute;
    left: 204px;
    top: 714px;
    width: 207px;
    height: 57px;
    border-radius: 4px;
    background: linear-gradient(var(--button-top) 0%, var(--button-top) 45%, var(--button-bottom) 100%);
    font-size: 34px;
    line-height: 55px;
    text-align: center;
    color: var(--text-light);
    white-space: nowrap;
  }
  .site-address {
    position: absolute;
    left: 0;
    top: 926px;
    width: 100%;
    text-align: center;
    font-size: 17px;
    line-height: 24px;
  }
</style>
</head>
<body>
  <main class="app-screen">
    <section class="welcome-panel">
      <h1 class="brand-title">NOVA GYM</h1>
      <p class="greeting">Bienvenido !</p>

      <div class="gender-option male" role="img" aria-label="Silhouette of a young man, selected male option"></div>
      <div class="gender-option female" role="img" aria-label="Silhouette of a young woman, female option"></div>

      <svg class="selected-tick" viewBox="0 0 44 44" aria-hidden="true">
        <circle cx="22" cy="22" r="20" fill="var(--tick-fill)" stroke="#ffffff" stroke-width="2.5"/>
        <path d="M12 22.5 L19.5 30 L33 14" fill="none" stroke="#ffffff" stroke-width="5" stroke-linecap="round" stroke-linejoin="round"/>
      </svg>

      <p class="intro-copy">Lorem ipsum dolor sit amet, consectetur adipisicing elit,<br>sed do eiusmod tempor incididunt ut labore et dolore magn<br>a aliqua. Ut enim ad minim veniam, quis nostrud exercitation</p>

      <div class="sign-on-button">Sign on !</div>

      <p class="site-address">www.novagym.com</p>
    </section>
  </main>
</body>
</html>
```